palduro.org business card design

We need 2-sided business cards for palduro.org; one side will be printed in English (EN), the other in Spanish (ES); the information represnted will be the same.
We are a non-profit that aims to mentor and coach future leaders / visionaries. Our target markets are developing countries (Latin America, Africa, Asia) rather than the developed ("western") world. Our business model works by finding funding to mentor / coach a candidate. We provide several mentors / coaches per candidate which help translate the candidate's vision / dream into a path with objectives and steps.
We want the business cards to transmit our values, which are: innovation, learning / self-improvement, equality (i.e. free from discrimination), boldness, intelligence, thoughtfulness, culture, society, future, sustainability.
We recommend the designers work with these values to produce a bold and innovative design, which does not need to adhere to the traditional criteria for business cards. Please use fresh (modern) colours.

Target Market(s)

Visionaries and thought leaders all over the world, but initially in Latin America. We don't discriminate on age, sex, religion, race or any other difference between people

Industry/Entity Type

Leadership

Contact Information for Business Card

The business cards will contain one language (English / Spanish) per side. It would be nice to have some continuity between the front and the back (e.g. pattern, colours).
Each side will contain the company name, website (www.palduro.org) and a slogan / mantra (which will be provided and can be represented as a placeholder until such time). The other details will be Name, (Function), and contact details (email and phone number).

Font styles to use
Sans Serif

Colors

Designer to choose colors to be used in the design.

Requirements
Must have
• [Side A: ENGLISH --- COMPANY INFO]
• [Company Name] Palduro
• [Slogan / Mantra] Shape your world!
• [Website] palduro.org
• [Side A: ENGLISH --- PERSONAL INFO]
• [Name] Tim Hallox
• [Job Title] Mentoring Coordinator
• [Phone / WhatsApp] +51 917 208 386
• [eMail] tim@palduro.org
• [Side B: SPANISH --- COMPANY INFO]
• [Company Name] Palduro
• [Slogan / Mantra] ¡Moldea tu mundo!
• [Website] palduro.org
• [Side B: SPANISH --- PERSONAL INFO]
• [Name] Timothy Hallox
• [Job Title] Coordinador de Mentoreo
• [eMail] tim@palduro.org
• [SIDE A: ENGLISH --- Central Values]
• - Future
• - Growth
• - Leadership
• [SIDE B: SPANISH --- Central Values]
• - Futuro
• - Liderazgo
• - Crecimiento
Nice to have
• Innovative and different design. Modern and fresh. Bold and clever.
• Secondary Values (we would like represented) are:
• [SIDE A: ENGLISH --- Secondary Values]
• - Equality
• - Innovation
• - Sustainability
• [SIDE B: SPANISH --- Secondary Values]
• - Igualdad
• - Innovación
• - Sostenibilidad
Should not have
• Please note that the images I have attached to this brief are just some images that I liked while browsing for material for the website. It does not imply I want these colours or this type of design, just that I felt these images had a good feel.

```html
<!DOCTYPE html>
<html lang="en">
<head>
<meta charset="utf-8">
<title>Palduro business cards</title>
<link href="https://fonts.googleapis.com/css2?family=Open+Sans:wght@400;600;700&family=Tinos&display=swap" rel="stylesheet">
<style>
  :root {
    --backdrop: #3a3a3a;
    --brand-blue: #1e80b8;
    --card-light: #e6e5e3;
    --band-light: #f2f2f2;
    --ink: #2b2b2b;
    --white: #ffffff;
  }
  * { margin: 0; padding: 0; box-sizing: border-box; }
  html, body {
    width: 1200px; height: 900px; overflow: hidden;
    background: var(--backdrop);
    font-family: "Open Sans", sans-serif;
  }
  .stage { position: relative; width: 1200px; height: 900px; }
  .card {
    position: absolute; top: 170px; width: 347px; height: 561px;
    box-shadow: 2px 3px 6px rgba(0,0,0,0.55);
    text-align: center; overflow: hidden;
  }
  .card--english { left: 259px; background: var(--card-light); color: var(--ink); }
  .card--spanish { left: 631px; background: var(--brand-blue); color: var(--white); }

  .brand { position: absolute; left: 0; right: 0; top: 98px; }
  .brand__name {
    font-weight: 700; font-size: 64px; line-height: 1; letter-spacing: 1px;
  }
  .brand__web {
    font-family: "Tinos", serif; font-size: 12px; letter-spacing: 4px; margin-top: 2px;
  }
  .card--english .brand__name, .card--english .brand__web { color: var(--brand-blue); }

  .person { position: absolute; left: 0; right: 0; top: 268px; }
  .person__name { font-weight: 700; font-size: 21px; line-height: 1.1; }
  .person__role { font-size: 14.5px; line-height: 1.3; }
  .card--english .person__name { color: var(--brand-blue); }

  .contact-icons {
    position: absolute; left: 0; right: 0; top: 330px;
    display: flex; justify-content: center; gap: 8px;
  }
  .contact-icons svg { width: 17px; height: 17px; display: block; }
  .card--english .contact-icons { color: var(--brand-blue); }
  .card--spanish .contact-icons { color: var(--white); }

  .contact-lines {
    position: absolute; left: 0; right: 0; top: 355px;
    font-size: 14.5px; line-height: 20px;
  }
  .values {
    position: absolute; left: 0; right: 0; top: 430px; font-size: 14.5px;
  }
  .values__sep { margin: 0 5px; }
  .card--english .values__sep { color: var(--brand-blue); }

  .slogan-band {
    position: absolute; left: 0; right: 0; bottom: 0;
    display: flex; align-items: center; justify-content: center;
    font-family: "Tinos", serif; font-size: 29px;
  }
  .card--english .slogan-band { height: 78px; background: var(--brand-blue); color: var(--white); }
  .card--spanish .slogan-band { height: 81px; background: var(--band-light); color: var(--brand-blue); }
</style>
</head>
<body>
<main class="stage">

  <section class="card card--english" lang="en">
    <div class="brand">
      <div class="brand__name">Palduro</div>
      <div class="brand__web">WWW.PALDURO.ORG</div>
    </div>
    <div class="person">
      <div class="person__name">TIMOTHY HALLOX</div>
      <div class="person__role">Coordinator Mentoring</div>
    </div>
    <div class="contact-icons" aria-hidden="true">
      <svg viewBox="0 0 20 20"><circle cx="10" cy="10" r="9" fill="currentColor"/></svg>
      <svg viewBox="0 0 20 20"><circle cx="10" cy="10" r="9.5" fill="currentColor"/><path d="M6.5 5.5l2 -.3 1 2.4-1.2 1a6 6 0 0 0 3 3l1-1.2 2.4 1-.3 2c-4.5.4-8.3-3.4-7.9-7.9z" fill="var(--card-light)"/></svg>
      <svg viewBox="0 0 20 20"><circle cx="10" cy="10" r="9.5" fill="currentColor"/><rect x="5" y="6.5" width="10" height="7" rx="1" fill="var(--card-light)"/><path d="M5.3 7l4.7 3.5 4.7-3.5" fill="none" stroke="currentColor" stroke-width="1"/></svg>
    </div>
    <div class="contact-lines">
      <div>+51 917 208 386</div>
      <div>+51 917 208 386</div>
      <div>tim@palduro.org</div>
    </div>
    <div class="values">Growth<span class="values__sep">|</span>Future<span class="values__sep">|</span>Leadership</div>
    <div class="slogan-band">Shape your world!</div>
  </section>

  <section class="card card--spanish" lang="es">
    <div class="brand">
      <div class="brand__name">Palduro</div>
      <div class="brand__web">WWW.PALDURO.ORG</div>
    </div>
    <div class="person">
      <div class="person__name">TIMOTHY HALLOX</div>
      <div class="person__role">Coordinador de Mentoreo</div>
    </div>
    <div class="contact-icons" aria-hidden="true">
      <svg viewBox="0 0 20 20"><circle cx="10" cy="10" r="9" fill="currentColor"/></svg>
      <svg viewBox="0 0 20 20"><circle cx="10" cy="10" r="9.5" fill="currentColor"/><path d="M6.5 5.5l2 -.3 1 2.4-1.2 1a6 6 0 0 0 3 3l1-1.2 2.4 1-.3 2c-4.5.4-8.3-3.4-7.9-7.9z" fill="var(--brand-blue)"/></svg>
      <svg viewBox="0 0 20 20"><circle cx="10" cy="10" r="9.5" fill="currentColor"/><rect x="5" y="6.5" width="10" height="7" rx="1" fill="var(--brand-blue)"/><path d="M5.3 7l4.7 3.5 4.7-3.5" fill="none" stroke="currentColor" stroke-width="1"/></svg>
    </div>
    <div class="contact-lines">
      <div>+51 917 208 386</div>
      <div>+51 917 208 386</div>
      <div>tim@palduro.org</div>
    </div>
    <div class="values">Crecimiento<span class="values__sep">|</span>Futuro<span class="values__sep">|</span>Liderazgo</div>
    <div class="slogan-band">Moldea tu mundo!</div>
  </section>

</main>
</body>
</html>
```